Gobal construction supply company needs new business card design

I need a business card design for my global supply company using an existing logo. i will be looking to print these on rounded corner cards with the black background version of my logo on the back. on the front white background, my logo again and my simple details.

```html
<!DOCTYPE html>
<html lang="en">
<head>
<meta charset="utf-8">
<title>Meridian Build Supply — Business Card</title>
<link rel="stylesheet" href="https://fonts.googleapis.com/css2?family=Open+Sans:wght@400;600;700&display=swap">
<style>
  :root {
    --backdrop: #2b2b2b;
    --card: #161616;
    --card-edge: #0d0d0d;
    --white: #f4f4f4;
    --red: #d8262e;
    --red-soft: #e0454c;
    --muted: #8a8a8a;
  }
  * { box-sizing: border-box; margin: 0; padding: 0; }
  html, body {
    width: 1200px; height: 716px; overflow: hidden;
    background: var(--backdrop);
    font-family: "Open Sans", Arial, sans-serif;
  }
  .canvas { position: relative; width: 1200px; height: 716px; }

  .card {
    position: absolute;
    width: 500px; height: 286px;
    border-radius: 22px;
    background: linear-gradient(160deg, #1c1c1c, var(--card));
    box-shadow: 0 3px 0 var(--card-edge), 0 18px 40px rgba(0,0,0,.45);
  }
  .card-back { left: 70px; top: 80px; }
  .card-front { left: 630px; top: 350px; }

  .brand { display: flex; align-items: center; gap: 10px; }
  .brand-name {
    font-weight: 700; font-size: 22px; letter-spacing: 1px;
    text-transform: uppercase; color: var(--white); line-height: 1;
  }
  .brand-dot { width: 12px; height: 12px; border-radius: 50%; background: var(--red); flex: none; }

  /* back */
  .card-back .brand { position: absolute; left: 0; right: 0; top: 112px; justify-content: center; }
  .card-back .brand-name { color: #5a5a5a; }
  .card-back .website {
    position: absolute; left: 0; right: 0; top: 178px; text-align: center;
    color: var(--red); font-size: 14px; letter-spacing: 2px;
  }

  /* front */
  .card-front .brand { position: absolute; left: 34px; top: 128px; }
  .card-front .brand-name { font-size: 18px; }
  .divider {
    position: absolute; left: 300px; top: 70px; width: 1px; height: 150px; background: var(--red);
  }
  .contact { position: absolute; left: 322px; top: 78px; }
  .person-name { color: var(--white); font-size: 27px; font-weight: 400; line-height: 1.1; }
  .job-title { color: var(--red); font-size: 12px; margin: 2px 0 16px; }
  .detail-list { list-style: none; }
  .detail {
    display: flex; align-items: center; gap: 8px;
    color: var(--white); font-size: 13px; margin-bottom: 8px;
  }
  .detail svg { width: 13px; height: 13px; flex: none; }
</style>
</head>
<body>
<main class="canvas">
  <section class="card card-back" aria-label="Card back">
    <div class="brand">
      <span class="brand-name">Meridian Build Supply</span>
      <span class="brand-dot"></span>
    </div>
    <p class="website">www.yourwebsite.com</p>
  </section>

  <section class="card card-front" aria-label="Card front">
    <div class="brand">
      <span class="brand-name">Meridian Build Supply</span>
      <span class="brand-dot"></span>
    </div>
    <div class="divider"></div>
    <div class="contact">
      <h1 class="person-name">Your Name</h1>
      <p class="job-title">Job Title</p>
      <ul class="detail-list">
        <li class="detail">
          <svg viewBox="0 0 16 16" aria-hidden="true"><path fill="#d8262e" d="M1 5c0-2 2-3 7-3s7 1 7 3v1h-4V5H5v1H1zM3 8h10l1 6H2zm5 1.5a2 2 0 100 4 2 2 0 000-4z"/></svg>
          000 000 0000
        </li>
        <li class="detail">
          <svg viewBox="0 0 16 16" aria-hidden="true"><rect x="1" y="3" width="14" height="10" fill="#d8262e"/><path d="M1 3l7 6 7-6" fill="none" stroke="#161616" stroke-width="1.3"/></svg>
          youremail@xyz.com
        </li>
        <li class="detail">
          <svg viewBox="0 0 16 16" aria-hidden="true"><g fill="none" stroke="#d8262e" stroke-width="1.3"><circle cx="8" cy="8" r="6.5"/><ellipse cx="8" cy="8" rx="2.8" ry="6.5"/><path d="M1.5 8h13M2.5 4.8h11M2.5 11.2h11"/></g></svg>
          www.yourwebsite.com
        </li>
      </ul>
    </div>
  </section>
</main>
</body>
</html>
```